Harbourline Refrigeration business card design

We would like a new design for our business card as we have a new logo.
We need generic business card to give our customers with our office details - with the option of making it individualized for each manager

Target Market(s)

Companies and homeowners

Industry/Entity Type

Air Conditioning

Contact Information for Business Card

We are not sure if we want single or double sided it will depend on the design we choose

Colors
33a6d7
0255a3

Requirements
Must have
• Logo
• phone: (08) 8721 5940
• email: harbourserve@tealnet.example
• website: www.harbourlinerefrigeration.example
• AU61420
• BLD472913
Nice to have
• Address - Shed 5/284 Tallis Rd, Kelbrook Vale SA 5799

```html
<!DOCTYPE html>
<html lang="en">
<head>
<meta charset="utf-8">
<title>Harbourline Refrigeration – Business Card</title>
<link href="https://fonts.googleapis.com/css2?family=Cinzel:wght@500&family=Libre+Baskerville:wght@700&family=Roboto:wght@400&display=swap" rel="stylesheet">
<style>
  :root {
    --bg: #e9ebee;
    --card: #ffffff;
    --blue-light: #33a6d7;
    --blue-deep: #0255a3;
    --navy-text: #0b2f55;
    --brand: #2a8fc9;
    --grey-text: #55606b;
    --tag-text: #4a4f55;
  }
  * { margin: 0; padding: 0; box-sizing: border-box; }
  html, body { width: 1200px; height: 1023px; overflow: hidden; background: var(--bg); }
  .stage { position: relative; width: 1200px; height: 1023px; }
  .card {
    position: absolute; left: 150px; top: 254px; width: 900px; height: 515px;
    background: var(--card); overflow: hidden;
    box-shadow: 0 14px 40px rgba(0,0,0,.18);
  }
  .card__swoosh { position: absolute; inset: 0; }
  .brand { position: absolute; left: 58px; top: 120px; }
  .brand__name {
    font-family: "Cinzel", serif; font-weight: 500; font-size: 44px;
    letter-spacing: 5px; color: var(--brand); line-height: 1;
  }
  .brand__tagline {
    margin-top: 10px; text-align: right;
    font-family: "Libre Baskerville", serif; font-weight: 700; font-size: 16px;
    letter-spacing: 1.5px; color: var(--tag-text);
  }
  .contacts { position: absolute; left: 70px; top: 300px; list-style: none; }
  .contacts li {
    display: flex; align-items: center; gap: 12px; height: 30px;
    font-family: "Roboto", sans-serif; font-size: 14px; color: var(--grey-text);
    white-space: nowrap;
  }
  .contacts svg { width: 16px; height: 16px; fill: var(--brand); flex: none; }
  .licences {
    position: absolute; right: 110px; top: 190px; text-align center;
    font-family: "Roboto", sans-serif; font-size: 22px; letter-spacing: 1.5px;
    color: var(--navy-text); line-height: 1.8; text-align: center;
  }
</style>
</head>
<body>
<main class="stage">
  <article class="card">
    <svg class="card__swoosh" viewBox="0 0 900 515" preserveAspectRatio="none" aria-hidden="true">
      <defs>
        <linearGradient id="panelBlue" x1="0" y1="1" x2="1" y2="0">
          <stop offset="0" stop-color="#33a6d7"/>
          <stop offset="0.55" stop-color="#1a82c6"/>
          <stop offset="1" stop-color="#0255a3"/>
        </linearGradient>
      </defs>
      <path d="M560,0 C545,220 480,400 380,515 L900,515 L900,0 Z" fill="#33a6d7"/>
      <path d="M572,0 C557,220 492,400 392,515 L900,515 L900,0 Z" fill="#ffffff"/>
      <path d="M586,0 C571,220 506,400 406,515 L900,515 L900,0 Z" fill="url(#panelBlue)"/>
    </svg>

    <div class="brand">
      <div class="brand__name">HARBOURLINE</div>
      <div class="brand__tagline">Refrigeration &amp; air conditioning</div>
    </div>

    <ul class="contacts">
      <li><svg viewBox="0 0 16 16"><path d="M3.5 1.5l2.5 3-1.5 1.5c.8 2 2.5 3.7 4.5 4.5L10.5 9l3 2.5-1.5 2.5C6.5 14 2 9.5 2 3z"/></svg>(08) 8721 5940</li>
      <li><svg viewBox="0 0 16 16"><path d="M1 3h14v10H1z M2 4l6 5 6-5" fill="none" stroke="#2a8fc9" stroke-width="1.5"/></svg>harbourserve@tealnet.example</li>
      <li><svg viewBox="0 0 16 16"><path d="M8 1a5 5 0 0 0-5 5c0 4 5 9 5 9s5-5 5-9a5 5 0 0 0-5-5zm0 7a2 2 0 1 1 0-4 2 2 0 0 1 0 4z"/></svg>Shed 5/284 Tallis Rd, Kelbrook Vale SA 5799</li>
      <li><svg viewBox="0 0 16 16"><g fill="none" stroke="#2a8fc9" stroke-width="1.3"><circle cx="8" cy="8" r="6.5"/><ellipse cx="8" cy="8" rx="3" ry="6.5"/><path d="M1.5 8h13M3 4.5h10M3 11.5h10"/></g></svg>www.harbourlinerefrigeration.example</li>
    </ul>

    <div class="licences">
      <div>AU61420</div>
      <div>BLD472913</div>
    </div>
  </article>
</main>
</body>
</html>
```